Toronto's Airline, based in Downtown looking for a whole new look and feel.

SkyVarn is looking for a new look in our website. We are an airline based at Corwen Haddle Airfield in Toronto. You can view our current website/services at www.skyvarn.example. We are expanding our services and look forward to a very sleek and modernized website. Please view the different pages on our website, we also need to add several new plane types as we have expanded and the website is not current. Would also be interesting to have a news feed or update feed through a widget which would be easy to use and update. we will also be implementing 2 third party programs called tolvo and quendrix on the website, both are tour based and airline based sales and management functions.

Target Market(s)

Commuters, travel, tourism, dates, general public

Industry/Entity Type

Airline

Coding

Coded - Design and coding required

Number of Pages Required

5+ page

Font styles to use
Other font styles liked:
• Toronto subway font would be nice

Requirements
Must have
• A modern feel, easy to use, our booking function is currently a bit confusing which we will be working on. Content can be taken from our current website www.skyvarn.example
Nice to have
• work with out theme colours of blue and light grey

```html
<!DOCTYPE html>
<html lang="en">
<head>
<meta charset="utf-8">
<title>SkyVarn Airways</title>
<link rel="stylesheet" href="https://fonts.googleapis.com/css2?family=Montserrat:wght@700&family=Open+Sans:wght@400;600&display=swap">
<style>
:root{
  --blue:#2f6db5;
  --blue-bright:#1f7bd0;
  --ink:#222;
  --text:#555;
  --muted:#777;
  --line:#d6d6d6;
  --panel:#f2f2f2;
  --card:#f6f5f5;
  --white:#fff;
  --footer:#f3f3f3;
}
*{box-sizing:border-box;margin:0;padding:0}
html,body{width:1200px;height:2616px;overflow:hidden;background:var(--white)}
body{position:relative;font-family:"Open Sans",Arial,sans-serif;color:var(--text)}
.abs{position:absolute}

/* header */
.site-header{left:0;top:0;width:1200px;height:100px}
.brand{left:91px;top:30px;display:flex;align-items:center;gap:10px}
.brand-mark{width:34px;height:34px;border:3px solid #6d7278;border-radius:50%}
.brand-name{font-size:24px;font-weight:600;color:#5d6369;letter-spacing:.5px}
.main-nav{left:350px;top:36px;display:flex;align-items:center;gap:0}
.main-nav a{font-size:14px;color:#444;text-decoration:none;text-transform:uppercase;padding:6px 14px;margin-right:6px}
.main-nav a.active{border:1px solid var(--blue);border-radius:16px;color:var(--blue)}
.main-nav a.cta{background:var(--blue);color:var(--white);border-radius:18px;font-size:13px;font-weight:600;padding:8px 14px}

/* hero */
.hero{left:0;top:100px;width:1200px;height:533px;background:linear-gradient(180deg,#5d6872 0%,#3f4a53 45%,#4d5761 100%)}
.hero-title{left:0;top:322px;width:1200px;text-align:center;font-family:Montserrat,Arial,sans-serif;font-size:41px;color:var(--white);letter-spacing:.5px}
.hero-sub{left:0;top:372px;width:1200px;text-align:center;font-size:25px;color:var(--white)}
.hero-arrow{top:380px}

/* booking */
.booking-title{left:91px;top:586px;width:1022px;height:47px;background:var(--blue);color:var(--white);font-size:26px;text-align:center;line-height:47px}
.booking-form{left:91px;top:633px;width:1022px;height:101px;background:var(--panel);box-shadow:0 2px 4px rgba(0,0,0,.12)}
.field-label{font-size:13px;color:#333}
.field{width:222px;height:37px;border:1px solid #aaa;background:var(--white);font-size:12px;color:#333;padding:0 10px;display:flex;align-items:center;justify-content:space-between}
.book-btn{left:905px;top:668px;width:173px;height:41px;border-radius:21px;background:var(--blue-bright);color:var(--white);font-size:19px;text-align:center;line-height:41px}

/* welcome */
.welcome-title{left:0;top:808px;width:1200px;text-align:center;font-size:29px;color:var(--ink)}
.welcome-text{left:186px;top:855px;width:828px;text-align:center;font-size:14px;line-height:22px;color:var(--muted)}
.service-card{top:970px;width:291px;height:280px;background:var(--white);box-shadow:0 1px 5px rgba(0,0,0,.18)}
.service-card .photo{width:291px;height:173px}
.service-card h3{margin-top:22px;text-align:center;font-size:16px;font-weight:400;color:var(--ink)}
.service-card p{margin:8px auto 0;width:250px;text-align:center;font-size:12px;line-height:19px;color:var(--muted)}

/* video */
.video{top:1339px;height:375px}
.play{left:50%;top:50%;width:62px;height:62px;margin:-31px 0 0 -31px;border-radius:50%;background:rgba(20,20,20,.75)}

/* news */
.news-title{left:0;top:1802px;width:1200px;text-align:center;font-size:29px;color:var(--ink)}
.news-item{width:499px;height:167px;background:var(--card);box-shadow:0 1px 4px rgba(0,0,0,.2);display:flex}
.news-item .photo{width:162px;height:167px;flex:none}
.news-body{padding:20px 24px 0 24px}
.news-body h4{font-size:15px;font-weight:400;color:#333}
.news-date{font-size:13px;color:#555;margin-top:6px}
.news-body p{font-size:11.5px;line-height:19px;color:#666;margin-top:4px}
.news-body a{font-size:12px;color:var(--blue-bright);text-decoration:none;display:block;margin-top:6px}

/* footer */
.site-footer{left:0;top:2337px;width:1200px;height:279px;background:var(--footer);border-top:2px solid var(--blue)}
.partner{font-size:26px;color:#2b3f5a;letter-spacing:3px}
.partner-b{display:flex;align-items:center;gap:8px;font-size:28px;font-weight:600;color:#2b3f5a}
.partner-b .dot{width:34px;height:34px;border-radius:50%;background:#2b3f5a}
.footer-head{font-size:15px;color:#333;text-transform:uppercase}
.footer-text{font-size:12px;line-height:22px;color:#666}
.mail-input{width:148px;height:31px;border:1px solid #bbb;background:var(--white);font-size:12px;color:#888;padding:0 8px;line-height:29px}
.mail-btn{width:56px;height:31px;background:var(--blue-bright);color:var(--white);font-size:12px;text-align:center;line-height:31px}
.social{width:24px;height:24px;border-radius:4px;background:#6a6a6a}
.footer-rule{left:86px;top:2548px;width:1022px;height:1px;background:var(--line)}
.copyright{left:0;top:2568px;width:1200px;text-align:center;font-size:12px;color:#333}
</style>
</head>
<body>

<header class="abs site-header">
  <div class="abs brand"><span class="brand-mark"></span><span class="brand-name">SkyVarn Airways</span></div>
  <nav class="abs main-nav">
    <a class="active">Home</a><a>Flights</a><a>Charter &amp; Fleet</a><a>Packages</a><a>Gallery</a><a>Contact</a><a>FAQ</a><a class="cta">Book Now</a>
  </nav>
</header>

<section class="abs hero" role="img" aria-label="Aerial photo of the Toronto skyline with the CN Tower and stadium, darkened"></section>
<h1 class="abs hero-title">SKYVARN AIRWAYS</h1>
<p class="abs hero-sub">Neque porro quisquam est qui dolorem</p>
<svg class="abs hero-arrow" style="left:74px" width="12" width2="" height="20" viewBox="0 0 12 20"><path d="M10 2 2 10l8 8" fill="none" stroke="#fff" stroke-width="2"/></svg>
<svg class="abs hero-arrow" style="left:1112px" width="12" height="20" viewBox="0 0 12 20"><path d="M2 2l8 8-8 8" fill="none" stroke="#fff" stroke-width="2"/></svg>

<div class="abs booking-title">BOOK NOW!</div>
<form class="abs booking-form">
  <span class="abs field-label" style="left:38px;top:20px">Enter Number of Passengers</span>
  <div class="abs field" style="left:38px;top:42px">2<svg width="10" height="6"><path d="M0 0h10L5 6z" fill="#222"/></svg></div>
  <span class="abs field-label" style="left:300px;top:20px">Choose a Date</span>
  <div class="abs field" style="left:300px;top:42px">15/May/2017<svg width="12" height="12" viewBox="0 0 12 12"><rect x="1" y="2" width="10" height="9" fill="none" stroke="#333"/><path d="M1 5h10M4 0v3M8 0v3" stroke="#333"/></svg></div>
  <span class="abs field-label" style="left:557px;top:20px">Choose a Time</span>
  <div class="abs field" style="left:557px;top:42px">12:30 PM - Available<svg width="10" height="6"><path d="M0 0h10L5 6z" fill="#222"/></svg></div>
</form>
<div class="abs book-btn">Book Now</div>

<h2 class="abs welcome-title">WELCOME TO SKYVARN AIRWAYS</h2>
<p class="abs welcome-text">It is a long established fact that a reader will be distracted by the readable content of a page when looking at its layout. The point of using Lorem Ipsum is that it has a more-or-less normal distribution of letters, as opposed to using 'Content here, content here', making it look like readable English. Many desktop publishing packages and web page editors</p>

<article class="abs service-card" style="left:134px">
  <div class="photo" role="img" aria-label="Aerial view of a harbour marina with boats" style="background:linear-gradient(160deg,#8fa7a9,#5f7d86 60%,#7a8c80)"></div>
  <h3>FLIGHTS</h3><p>It has survived not only five centuries, but also the leap into electronic</p>
</article>
<article class="abs service-card" style="left:455px">
  <div class="photo" role="img" aria-label="Bright lounge with chair and desk overlooking a waterfront" style="background:linear-gradient(180deg,#b9d3ea,#d8dde2 55%,#8a8580)"></div>
  <h3>PRIVATE CHARTER</h3><p>It has survived not only five centuries, but also the leap into electronic</p>
</article>
<article class="abs service-card" style="left:774px">
  <div class="photo" role="img" aria-label="Glass skyscraper lit at night" style="background:linear-gradient(160deg,#1a1f2a,#3b5270 55%,#141820)"></div>
  <h3>PACKAGES</h3><p>It has survived not only five centuries, but also the leap into electronic</p>
</article>

<div class="abs video" style="left:0;width:600px;background:linear-gradient(180deg,#a9c3d8 0%,#8e9da6 45%,#b4aa98 75%,#8f8677 100%)" role="img" aria-label="Video: twin-engine aircraft on the tarmac in front of the Toronto skyline">
  <svg class="abs play" viewBox="0 0 62 62"><path d="M24 18l20 13-20 13z" fill="#fff"/></svg>
</div>
<div class="abs video" style="left:602px;width:598px;background:linear-gradient(160deg,#6f8a94 0%,#4a4f52 45%,#c9ccce 100%)" role="img" aria-label="Video: happy couple beside a white car">
  <svg class="abs play" viewBox="0 0 62 62"><path d="M24 18l20 13-20 13z" fill="#fff"/></svg>
</div>

<h2 class="abs news-title">LATEST NEWS</h2>
<article class="abs news-item" style="left:91px;top:1877px">
  <div class="photo" role="img" aria-label="Aerial view of wooded islands on a lake" style="background:linear-gradient(160deg,#5c7f92,#3f6b4a 60%,#4f7a8c)"></div>
  <div class="news-body"><h4>Nemo Enim Ipsam Volup</h4><div class="news-date">09-07-2017</div><p>Lorem Ipsum has been the industry's standard dummy text ever since the 1500s, when an unknown printer took a galley of type and scrambled it to make</p><a>Read More &gt;&gt;</a></div>
</article>
<article class="abs news-item" style="left:614px;top:1877px">
  <div class="photo" role="img" aria-label="Aerial view of downtown towers" style="background:linear-gradient(170deg,#b7c4cf,#6b6660 60%,#8a7a6a)"></div>
  <div class="news-body"><h4>Dolorem ipsum quia</h4><div class="news-date">09-07-2017</div><p>Lorem Ipsum has been the industry's standard dummy text ever since the 1500s, when an unknown printer took a galley of type and scrambled it to make</p><a>Read More &gt;&gt;</a></div>
</article>
<article class="abs news-item" style="left:91px;top:2067px">
  <div class="photo" role="img" aria-label="Couple seated in a private aircraft cabin" style="background:linear-gradient(160deg,#3a3430,#8b7868 55%,#d6cbbf)"></div>
  <div class="news-body"><h4>Quisquam est qui dolorem ipsum</h4><div class="news-date">09-07-2017</div><p>Lorem Ipsum has been the industry's standard dummy text ever since the 1500s, when an unknown printer took a galley of type and scrambled it to make</p><a>Read More &gt;&gt;</a></div>
</article>
<article class="abs news-item" style="left:614px;top:2067px">
  <div class="photo" role="img" aria-label="Aerial view of a city neighbourhood" style="background:linear-gradient(170deg,#c5ccd2,#8a8c82 50%,#6f7566)"></div>
  <div class="news-body"><h4>Porro quisquam est qui dolorem</h4><div class="news-date">09-07-2017</div><p>Lorem Ipsum has been the industry's standard dummy text ever since the 1500s, when an unknown printer took a galley of type and scrambled it to make</p><a>Read More &gt;&gt;</a></div>
</article>

<footer class="abs site-footer">
  <div class="abs partner" style="left:91px;top:72px">QUENDRIX</div>
  <div class="abs partner-b" style="left:91px;top:112px"><span class="dot"></span>tolvo</div>

  <h5 class="abs footer-head" style="left:344px;top:53px">Contact Us</h5>
  <div class="abs footer-text" style="left:344px;top:88px;width:260px">Address : Corwen Haddle Airfield<br>Hangar 4, Suite 210 Toronto, Ontario M0X 2B7<br>Phone : 1-800-555-0142<br>Email : info@skyvarn.example</div>

  <h5 class="abs footer-head" style="left:659px;top:53px">Join Our Mailing List</h5>
  <div class="abs footer-text" style="left:659px;top:82px;width:210px;line-height:18px">Your about us information would fit here nicely.</div>
  <div class="abs mail-input" style="left:659px;top:133px">Email address</div>
  <div class="abs mail-btn" style="left:807px;top:133px">Submit</div>

  <h5 class="abs footer-head" style="left:947px;top:53px">Follow Us Out There</h5>
  <span class="abs social" style="left:950px;top:98px"></span>
  <span class="abs social" style="left:988px;top:98px"></span>
  <span class="abs social" style="left:1026px;top:98px"></span>
  <span class="abs social" style="left:1064px;top:98px"></span>
</footer>
<div class="abs footer-rule"></div>
<p class="abs copyright">Copyright © 2017. All Rights Reserved</p>

</body>
</html>
```